Business Card Design

I am a cosmetic tattooist in Melbourne Australia, who provides services where by I tattoo eyebrows in block or strokes with a tattooing gun. Feathering that mimic hair strands with a scalpel. Eyeliner top and bottom with the tattooing gun. Lips just as either an outline or a full block colour where the top and bottom lip is completely covered. Corrections for tattooing done previously that have either faded to quickly, turned blue or orange due to bad colour choice, or a mishap. Paramedical colouring for people who either have scaring that needs to be matched to their skin colour. Patients who have alopecia or a skin condition that needs hair like tattooing. Cancer patients who's nipples and areolas have been partially or totally been removed and require them to be re drawn into the new skin. I colour match with a variety of inks (around 50) at my disposal and can also lift colours with a pigmentation lifter. I also require the use of two different types of anaesthetics throughout each procedure.
Colours that I have looked into the represent health, professionalism, beauty, skin and medical type procedures are Light to dark brown, Light to dark grey, Black and White. Possibly a splash of red to represent the lips. I am mobile and can work from any venue that takes a commission for a bed. I have completed a diploma in cosmetic tattooing being qualified.
Updates

Project Deadline Extended
Reason: I have been awaiting for a design from own more designer who accepted my project but hasn't released their design.

Project Deadline Extended

Industry/Entity Type

Medical

Contact Information for Business Card

Company name: Velvet Arch Cosmetic Tattooing
Name: Lorna Beswick
Title: Cosmetic and Paramedical Tattooist
Address: P.O Box 2863, Ashmont Heights, Victoria 3297
Mobile: 0417365821
Email: velvetarchtattooing@quillmail.example
Preferred colours: Light brown, Light Grey, Black (writing) White Background

Requirements
Nice to have
• A shape of the eyebrow or eye with eyeliner in the background. Possibly red lips. No straight lines, only curved or curled lines.

```html
<!DOCTYPE html>
<html lang="en">
<head>
<meta charset="utf-8">
<title>Velvet Arch Cosmetic Tattooing – Business Card</title>
<link rel="stylesheet" href="https://fonts.googleapis.com/css2?family=Open+Sans:wght@400;600&family=Arimo:wght@400&display=swap">
<style>
  :root {
    --page-bg: #e9e6e2;
    --card-white: #ffffff;
    --accent-red: #c8221f;
    --accent-red-mid: #e2644d;
    --accent-red-soft: #f4b8a3;
    --band-red: #bd1f1d;
    --ink: #141414;
    --ink-soft: #2a2a2a;
    --photo-dark: #6f7274;
    --photo-mid: #b9bcbe;
    --photo-light: #f4f5f5;
  }
  * { margin: 0; padding: 0; box-sizing: border-box; }
  html, body {
    width: 1200px; height: 1200px; overflow: hidden;
    background: var(--page-bg);
  }
  .card {
    position: absolute;
    left: 60px; top: 269px;
    width: 1080px; height: 662px;
    background: linear-gradient(90deg,
      var(--accent-red) 0%,
      var(--accent-red-mid) 11%,
      var(--accent-red-soft) 24%,
      var(--card-white) 40%,
      var(--card-white) 100%);
    overflow: hidden;
  }
  .card__band {
    position: absolute; left: 0; bottom: 0;
    width: 100%; height: 22px;
    background: var(--band-red);
  }
  .eye-photo {
    position: absolute; left: 600px; top: 22px;
    width: 480px; height: 495px;
    z-index: 0;
    background:
      radial-gradient(ellipse 60% 34% at 58% 40%, var(--photo-dark) 0%, var(--photo-mid) 45%, transparent 75%),
      radial-gradient(ellipse 70% 60% at 60% 40%, var(--photo-light) 0%, var(--card-white) 80%);
  }
  .brand {
    position: absolute; left: 48px; top: 128px;
    z-index: 1;
    font-family: "Open Sans", sans-serif;
    font-weight: 600;
    color: var(--ink);
    white-space: nowrap;
  }
  .brand__line { display: block; }
  .brand__line--first { font-size: 47px; line-height: 54px; }
  .brand__line--second {
    font-size: 60px; line-height: 68px;
    margin-top: 40px;
    padding-left: 124px;
  }
  .holder {
    position: absolute; left: 57px; top: 388px;
    z-index: 1;
    font-family: "Open Sans", sans-serif;
    color: var(--ink);
    white-space: nowrap;
  }
  .holder__name { font-size: 32px; font-weight: 600; line-height: 44px; }
  .holder__title { font-size: 23px; font-weight: 400; line-height: 36px; color: var(--ink-soft); }
  .contacts {
    position: absolute; left: 56px; top: 488px;
    z-index: 1;
    list-style: none;
    font-family: "Arimo", sans-serif;
    font-size: 24px; color: var(--ink);
    white-space: nowrap;
  }
  .contacts__item {
    display: flex; align-items: center;
    height: 45px;
  }
  .contacts__icon { width: 30px; height: 30px; margin-right: 20px; flex: none; }
</style>
</head>
<body>
  <main class="card">
    <div class="eye-photo" role="img" aria-label="Close-up photograph of an eye with long lashes and glittering eye shadow"></div>

    <h1 class="brand">
      <span class="brand__line brand__line--first">Velvet Arch Cosmetic</span>
      <span class="brand__line brand__line--second">Tattooing</span>
    </h1>

    <section class="holder">
      <p class="holder__name">Lorna Beswick</p>
      <p class="holder__title">Cosmetic and Paramedical Tattooist</p>
    </section>

    <ul class="contacts">
      <li class="contacts__item">
        <svg class="contacts__icon" viewBox="0 0 30 30" aria-hidden="true">
          <circle cx="15" cy="15" r="15" fill="#141414"/>
          <path d="M15 7a5.5 5.5 0 0 0-5.5 5.5c0 4 5.5 10 5.5 10s5.5-6 5.5-10A5.5 5.5 0 0 0 15 7z" fill="none" stroke="#fff" stroke-width="2"/>
          <circle cx="15" cy="12.5" r="2" fill="#fff"/>
        </svg>
        <span>P.O Box 2863, Ashmont Heights, Victoria 3297</span>
      </li>
      <li class="contacts__item">
        <svg class="contacts__icon" viewBox="0 0 30 30" aria-hidden="true">
          <circle cx="15" cy="15" r="15" fill="#141414"/>
          <path d="M10.5 8.5l2.6-.6 1.6 3.6-1.8 1.3a9 9 0 0 0 4.3 4.3l1.3-1.8 3.6 1.6-.6 2.6c-.3 1-1.3 1.6-2.3 1.4A13 13 0 0 1 9 10.8c-.2-1 .4-2 1.5-2.3z" fill="#fff"/>
        </svg>
        <span>0417365821</span>
      </li>
      <li class="contacts__item">
        <svg class="contacts__icon" viewBox="0 0 30 30" aria-hidden="true">
          <circle cx="15" cy="15" r="15" fill="#141414"/>
          <rect x="7.5" y="10" width="15" height="10.5" rx="1" fill="#fff"/>
          <path d="M8 10.8l7 5.2 7-5.2" fill="none" stroke="#141414" stroke-width="1.5"/>
        </svg>
        <span>velvetarchtattooing@quillmail.example</span>
      </li>
    </ul>

    <div class="card__band"></div>
  </main>
</body>
</html>
```